The Copper Ladder

we require a classy business card design for a business coaching company that uses our current logo and the wording:

Front of card:

LOGO
Kyle Morrison
CEO
TEL: 1300 4 52918
FAX: 1300 5 52918
Mobile: 0412 638194
PO Box 917, Ferris Hollow, Brisbane, Qld 4127
e: kylem@copperladder.com.au
w: www.copperladder.com.au

Reverse side of the card:

Systematizing Businesses into Turnkey Operations
Strategic Business Plans
Sales & Marketing Programs
Sales Training & Business Coaching
Internet Marketing & Web Design

Here’s what our clients say:

“We grew from $396,000 to over $5million in 4 years and made KTS’s Rising Enterprises Roll 3 years running!” – Martin Greaves, Meridian Works

Target Market(s)

small to medium sized business owners in Australia

Industry/Entity Type

Business

Requirements
Must have
• standard business card size

```html
<!DOCTYPE html>
<html lang="en">
<head>
<meta charset="utf-8">
<title>The Copper Ladder – Business Card</title>
<link rel="stylesheet" href="https://fonts.googleapis.com/css2?family=Tinos&family=Noto+Sans:wght@400;700&display=swap">
<style>
  :root {
    --page-bg: #ffffff;
    --card-bg: #ffffff;
    --card-edge: #9a9a9a;
    --card-shadow: #4a4a4a;
    --band-red: #e3121b;
    --band-maroon: #5a1414;
    --ink: #1e1e1e;
    --ink-soft: #5a5a5a;
    --accent-red: #d8141c;
    --address-red: #cc1010;
    --star-pink: #e77f8e;
    --star-light: #f6d3d8;
  }
  html, body {
    margin: 0;
    width: 1200px;
    height: 900px;
    overflow: hidden;
    background: var(--page-bg);
  }
  .canvas {
    position: relative;
    width: 1200px;
    height: 900px;
  }
  .business-card {
    position: absolute;
    left: 147px;
    top: 190px;
    width: 748px;
    height: 436px;
    background: var(--card-bg);
    border: 2px solid var(--card-edge);
    box-shadow: 4px 4px 0 var(--card-shadow);
    box-sizing: border-box;
  }
  .side-band {
    position: absolute;
    top: 10px;
    height: 412px;
  }
  .side-band--red { left: 8px; width: 21px; background: var(--band-red); }
  .side-band--maroon { left: 29px; width: 17px; background: var(--band-maroon); }

  .company-name {
    position: absolute;
    left: 182px;
    top: 58px;
    margin: 0;
    font-family: "Tinos", "Times New Roman", serif;
    font-weight: 400;
    font-size: 54px;
    line-height: 1;
    color: var(--ink);
    white-space: nowrap;
  }
  .star-art {
    position: absolute;
    left: 85px;
    top: 106px;
    width: 116px;
    height: 112px;
    border-radius: 50%;
    background: radial-gradient(circle at 45% 45%, var(--star-light), var(--star-pink) 70%, transparent 72%);
  }
  .person {
    position: absolute;
    left: 264px;
    top: 134px;
    font-family: "Noto Sans", Verdana, sans-serif;
    font-weight: 700;
    font-size: 27px;
    line-height: 43px;
    color: var(--ink);
  }
  .person p { margin: 0; }
  .divider {
    position: absolute;
    left: 96px;
    top: 222px;
    width: 548px;
    height: 4px;
    background: var(--accent-red);
  }
  .phone-list {
    position: absolute;
    left: 92px;
    top: 244px;
    margin: 0;
    padding: 0;
    list-style: none;
    font-family: "Tinos", "Times New Roman", serif;
    font-size: 20px;
    line-height: 25px;
    color: var(--ink-soft);
  }
  .postal-address {
    position: absolute;
    left: 331px;
    top: 244px;
    margin: 0;
    font-style: normal;
    font-family: "Tinos", "Times New Roman", serif;
    font-size: 32px;
    line-height: 40px;
    color: var(--address-red);
    white-space: nowrap;
  }
  .online-contact {
    position: absolute;
    left: 92px;
    top: 335px;
    margin: 0;
    font-family: "Noto Sans", Verdana, sans-serif;
    font-size: 27px;
    line-height: 40px;
    color: var(--ink);
  }
  .online-contact p { margin: 0; }
</style>
</head>
<body>
<main class="canvas">
  <section class="business-card" aria-label="Business card front">
    <div class="side-band side-band--red"></div>
    <div class="side-band side-band--maroon"></div>

    <h1 class="company-name">The Copper Ladder</h1>

    <div class="star-art" role="img" aria-label="Pink star emblem"></div>

    <div class="person">
      <p class="person-name">Kyle Morrison</p>
      <p class="person-title">CEO</p>
    </div>

    <div class="divider"></div>

    <ul class="phone-list">
      <li>TEL: 1300 4 52918</li>
      <li>FAX: 1300 5 52918</li>
      <li>Mobile: 0412 638194</li>
    </ul>

    <address class="postal-address">PO Box 917, Ferris Hollow,<br>Brisbane, Qld 4127</address>

    <div class="online-contact">
      <p>Email: kylem@copperladder.com.au</p>
      <p>Website: www.copperladder.com.au</p>
    </div>
  </section>
</main>
</body>
</html>
```